French flying club (aeroclub) complete wordpress theme

We need a complete wordpress theme to overhaul the look and feel of our aeroclub website.

We are a flying club (aeroclub) based in France, near Paris. We are a non-profit organization providing VFR flight training to members of all ages; our instructors all have extensive experience flying professionally (one of them was captain on the Stratoline!) We have a fleet of 3 aircraft of the same type (Pelvo) that we provide to our members at competitive rates: since we are a non-profit, there are no unnecessary margins on what we charge aside from what’s necessary for renewal of a fun-to-fly fleet!

The club has a very old history (founded in 1950), and was initially founded by female pioneers of aviation in France (corps founded in 1934), serving as flying nurses for the French army in various conflicts and for search-and-rescue missions. Now of course we accept all types of applicants! Our members are genuinely passionate about flying, they care more about time airborne than about the glamour surrounding aviation (not that it does not matter).

We are launching this website design contest because our current website (http://www.aeroclub-kelvo.org/) is somewhat stuck in the ‘90s, and we’d like to give it a new look and feel.

Some designs that caught our attention, to draw inspiration from:
- http://www.volbrumeclub.fr/
- http://www.cieldutal.com/
- http://www.ecole-varnot.com/

Idea would be to provide front page access to the latest pictures and movies taken from our latest flights, a few breaking news, and one click access to a few sections, e.g.:
- our fleet/prices
- instruction options (VFR, night VFR, BIA etc.)
- location and contact info
- history
- a members-private login page for aircraft reservation and planning access, supporting some sort of forum/message board would etc.

When it comes to style, we’re looking for things that relate to our logo colors (blue dominant with some red and white). Our logo can be found at http://www.aeroclub-kelvo.org/images/banners_logos/logo_kelvo.gif (we can provide a higher resolution one upon request).

Attached are a few excerpts from existing pages (zip file). They're in French but content is usually self-explanatory. Explanations can be provided if necessary.

Target Market(s)

We tend to have various ‘segments’ of users:
- Teenagers and young adults looking to learn flying
- Seniors looking to learn flying
- Experienced pilots who are looking for a no-nonsense, flying enthusiast community

Industry/Entity Type

Club

Font styles to use
Sans Serif

Requirements
Must have
• Theme should be supplied as a self-deployable wordpress package that can be deployed on a fresh instance of wordpress (i.e. wordpress-compatible zip archive)

```html
<!DOCTYPE html>
<html lang="en">
<head>
<meta charset="utf-8">
<title>Aéro club des Kelvo</title>
<link rel="stylesheet" href="https://fonts.googleapis.com/css2?family=Raleway:wght@400;500;600&display=swap">
<style>
  :root {
    --blue: #3d9fd6;
    --blue-dark: #1f6fa8;
    --red: #d9343a;
    --ink: #4a4a4a;
    --muted: #8a8a8a;
    --line: #d6d6d6;
    --nav: rgba(60, 64, 70, 0.82);
    --footer: #3e3f42;
    --page: #ffffff;
  }
  * { box-sizing: border-box; margin: 0; padding: 0; }
  html, body { width: 885px; height: 1200px; overflow: hidden; background: var(--page); }
  body { font-family: "Raleway", sans-serif; color: var(--ink); position: relative; }

  .site-header { position: absolute; top: 0; left: 0; width: 885px; height: 165px; }
  .brand-mark {
    position: absolute; left: 412px; top: 14px; width: 62px; height: 62px;
    border-radius: 50%; border: 3px solid var(--blue); background: #eef6fc;
  }
  .brand-name {
    position: absolute; top: 98px; left: 0; width: 885px; text-align: center;
    font-size: 40px; font-weight: 500; color: var(--blue); letter-spacing: 1px;
  }
  .login-button {
    position: absolute; top: 6px; left: 778px; width: 26px; height: 26px;
    border: 2px solid var(--red); border-radius: 6px; background: #fff;
  }

  .hero {
    position: absolute; top: 165px; left: 0; width: 885px; height: 265px;
    background: linear-gradient(180deg, #5f7fa6 0%, #a9c0d8 45%, #e9eef4 75%, #cfd9e4 100%);
  }
  .main-nav {
    position: absolute; top: 165px; left: 0; width: 885px; height: 24px;
    background: var(--nav); display: flex; justify-content: center; gap: 38px;
    align-items: center;
  }
  .main-nav a {
    color: #f1f1f1; text-decoration: none; font-size: 10px; font-weight: 500; letter-spacing: .6px;
  }

  .section-title {
    position: absolute; left: 0; width: 885px; text-align: center;
    font-size: 17px; font-weight: 500; letter-spacing: 1px; color: #555;
  }
  .gallery-title { top: 452px; }
  .news-title { top: 722px; }

  .thumb { position: absolute; top: 495px; width: 216px; height: 135px; }
  .thumb-hangar { left: 80px; background: linear-gradient(180deg, #8fb2d8 0%, #b7c6d3 55%, #8a8f8a 100%); }
  .thumb-cockpit { left: 334px; background: linear-gradient(180deg, #3a3d42 0%, #23272b 60%, #4c5660 100%); }
  .thumb-video { left: 590px; background: linear-gradient(180deg, #7fa7d6 0%, #b8cde0 55%, #9b9c96 100%); }
  .play-icon { position: absolute; left: 90px; top: 49px; }

  .more-button {
    position: absolute; left: 402px; width: 82px; height: 20px;
    border: 1px solid var(--blue); border-radius: 10px; color: var(--blue);
    font-size: 9px; letter-spacing: 1px; text-align: center; line-height: 18px; background: #fff;
  }
  .gallery-more { top: 664px; }
  .news-more { top: 1045px; }

  .divider { position: absolute; top: 700px; left: 40px; width: 805px; height: 1px; background: var(--line); }

  .news-item-title { position: absolute; top: 780px; left: 80px; font-size: 14px; font-weight: 600; color: #444; }
  .news-item-text { position: absolute; top: 806px; left: 80px; width: 310px; font-size: 10px; line-height: 14px; color: var(--muted); }
  .news-item-text p { margin-bottom: 9px; }
  .news-photo {
    position: absolute; top: 760px; left: 482px; width: 323px; height: 225px;
    background: linear-gradient(180deg, #8db4de 0%, #c3d3e2 45%, #a7a79e 75%, #7c8a72 100%);
  }

  .slider-dots { position: absolute; top: 1000px; left: 429px; display: flex; gap: 5px; }
  .slider-dots span { width: 6px; height: 6px; border-radius: 50%; background: #c9d6e0; }
  .slider-dots span.active { background: var(--blue); }

  .site-footer { position: absolute; top: 1145px; left: 0; width: 885px; height: 55px; background: var(--footer); }
</style>
</head>
<body>
  <header class="site-header">
    <div class="brand-mark"></div>
    <div class="brand-name">Aéro club des Kelvo</div>
    <div class="login-button" aria-label="Member login"></div>
  </header>

  <div class="hero" role="img" aria-label="Light aircraft flying above the clouds"></div>
  <nav class="main-nav">
    <a href="#">HOME</a>
    <a href="#">OUR FLEET/PRICES</a>
    <a href="#">INSTRUCTION OPTIONS</a>
    <a href="#">LOCATION AND CONTACT INFO</a>
    <a href="#">HISTORY</a>
  </nav>

  <h2 class="section-title gallery-title">OUR GALLERY</h2>
  <div class="thumb thumb-hangar" role="img" aria-label="Club aircraft parked in front of the hangar"></div>
  <div class="thumb thumb-cockpit" role="img" aria-label="Cockpit instrument panel"></div>
  <div class="thumb thumb-video" role="img" aria-label="Video of a club aircraft on the apron">
    <svg class="play-icon" width="36" height="36" viewBox="0 0 36 36" aria-hidden="true">
      <circle cx="18" cy="18" r="17" fill="#3d9fd6"/>
      <path d="M14 11 L26 18 L14 25 Z" fill="#fff"/>
    </svg>
  </div>
  <div class="more-button gallery-more">MORE</div>

  <div class="divider"></div>

  <h2 class="section-title news-title">LAST NEWS</h2>
  <h3 class="news-item-title">Some text little</h3>
  <div class="news-item-text">
    <p>Our three Pelvo aircraft flew twenty hours this month. Thanks to every member who helped with the spring cleaning and the hangar repairs.</p>
    <p>Night VFR sessions restart in May. Ask an instructor to book your first slot, and bring your logbook to the briefing room before each flight.</p>
    <p>Our open day takes place on Saturday. Families are welcome to visit the fleet and meet our volunteers.</p>
  </div>
  <div class="news-photo" role="img" aria-label="Club aircraft on the grass beside the hangar"></div>
  <div class="slider-dots"><span class="active"></span><span></span><span></span><span></span></div>
  <div class="more-button news-more">MORE</div>

  <footer class="site-footer"></footer>
</body>
</html>
```